Plastic Seasoning Bottle Design Label

I am looking to get a label design that's going on plastic seasoning bottles. My company which deals with seasons/spices. My company sells healthy all natural seasons so I would like the label to have a design of natural. I also would like a hot pepper on there showing it's hot and also other red indentations like red fire or something that shows it's very hot !!!
The company name is Brisk Meadow Harvest which I would like in light green letters.
There are six different seasonings favors which are:
Barbecue
Garlic
Lemon
Chili
Poultry/Meat
Seafood

The label size: 190.00mm x 111.00mm

Thanks

I would like for the colors to be:
Green
Light Green
Red ( For Hot )
White
Seafood
All of them will be hot as it will show on the label.

Hello, Please include on the labels pictures of the foods associated with the seasoning. Example: Seafood= Fish,lobster,clams,shrimp,scallops,eel,octopus,squid and muscles which will show that it's also very hot. As for seasonings like the Lemon you could just put pictures of lemons which are showing also that there hot as all of the seasoning are hot also. Garlic would be the same as the lemon with just picture also showing it's very hot. Meat would show different kinds of beef such as steak,hamburgers. Also chicken and ham which will show that it's also very hot. Barbecue and Chili you can feel free to show different ideas on that as they will also show that they are very hot as all of them are. The label size is 190.00mm x 111.00mm If you need more time to work on this project please feel free to let me know as I have no problem extending the dead line. Thanks

Hello, In the last update I mentioned Ham as I met to put Ribs not Ham. Thanks

Hello, The budget has been increased. It's now 201.00

Hello, At the end of the company name I would like to have a small TM at the end of the company name as the the has a trade mark on it. Thanks

Industry/Entity Type

Plastic

Font styles to use
Serif
Sans Serif
Decorative
Script
Other font styles liked:
• Georgia,Italic,Bold

```html
<!DOCTYPE html>
<html lang="en">
<head>
<meta charset="utf-8">
<title>Brisk Meadow Harvest – Seasoning Labels</title>
<link rel="stylesheet" href="https://fonts.googleapis.com/css2?family=Gelasio:wght@400;700&family=Tinos:wght@400;700&family=Pinyon+Script&display=swap">
<style>
  :root {
    --canvas: #ffffff;
    --label-top: #fff3e2;
    --label-mid: #f9c3a2;
    --label-bottom: #f07a62;
    --border-red: #d8322a;
    --brand-green: #5fdc3c;
    --ink: #111111;
    --burst-yellow: #f4e23a;
    --burst-edge: #e0b81a;
    --flame-red: #e0281a;
    --flame-orange: #f4791c;
    --flame-yellow: #fbc93a;
  }
  * { box-sizing: border-box; margin: 0; padding: 0; }
  html, body { width: 667px; height: 1200px; overflow: hidden; background: var(--canvas); }
  .sheet { position: relative; width: 667px; height: 1200px; }
  .label {
    position: absolute; left: 0; width: 667px; height: 392px; overflow: hidden;
    background: linear-gradient(180deg, var(--label-top) 0%, var(--label-mid) 50%, var(--label-bottom) 100%);
  }
  .label--garlic { top: 0; }
  .label--meat { top: 404px; }
  .label--chili { top: 808px; }
  .flames {
    position: absolute; left: 0; top: 0; width: 667px; height: 270px;
    background:
      radial-gradient(ellipse 22% 75% at 6% 40%, var(--flame-red) 0%, var(--flame-orange) 40%, var(--flame-yellow) 65%, transparent 85%),
      radial-gradient(ellipse 22% 75% at 94% 40%, var(--flame-red) 0%, var(--flame-orange) 40%, var(--flame-yellow) 65%, transparent 85%),
      radial-gradient(ellipse 18% 55% at 24% 20%, var(--flame-orange) 0%, var(--flame-yellow) 55%, transparent 80%),
      radial-gradient(ellipse 18% 55% at 76% 20%, var(--flame-orange) 0%, var(--flame-yellow) 55%, transparent 80%),
      radial-gradient(ellipse 30% 40% at 50% 0%, var(--flame-orange) 0%, var(--flame-yellow) 50%, transparent 85%);
  }
  .cut-line { position: absolute; inset: 9px; border: 2px dashed var(--border-red); pointer-events: none; }
  .brand {
    position: absolute; top: 14px; left: 0; width: 100%; text-align: center;
    font-family: "Gelasio", Georgia, serif; font-size: 27px; color: var(--brand-green);
  }
  .brand sup { font-size: 11px; }
  .kicker {
    position: absolute; font-family: "Tinos", "Times New Roman", serif;
    font-size: 20px; letter-spacing: .5px; color: var(--ink); white-space: nowrap;
  }
  .flavor {
    position: absolute; font-family: "Pinyon Script", cursive; color: var(--ink);
    white-space: nowrap; line-height: 1;
  }
  .food-photo { position: absolute; border-radius: 10px; }
  .badge { position: absolute; left: 0; width: 128px; height: 128px; }
  .badge svg { position: absolute; inset: 0; }
  .badge-text {
    position: absolute; left: 12px; top: 44px; width: 110px;
    font-family: "Tinos", "Times New Roman", serif; font-weight: 700; font-size: 13px; line-height: 1.25; color: var(--ink);
  }
</style>
</head>
<body>
<main class="sheet">

  <section class="label label--garlic">
    <div class="flames" role="img" aria-label="Red, orange and yellow fire flames rising across the label"></div>
    <div class="cut-line"></div>
    <p class="brand">Brisk Meadow Harvest<sup>TM</sup></p>
    <span class="kicker" style="left:226px;top:90px;">NATURAL</span>
    <span class="flavor" style="left:220px;top:116px;font-size:110px;">Garlic</span>
    <span class="kicker" style="left:296px;top:210px;">SEASONING</span>
    <div class="badge" style="top:186px;">
      <svg viewBox="0 0 128 128"><polygon points="64,2 76,34 108,16 96,50 126,64 96,78 108,112 76,94 64,126 52,94 20,112 32,78 2,64 32,50 20,16 52,34" fill="var(--burst-yellow)" stroke="var(--burst-edge)" stroke-width="2"/></svg>
      <p class="badge-text">HEALTHY &amp;<br>ALL NATURAL</p>
    </div>
    <div class="food-photo" role="img" aria-label="Photo of two whole garlic bulbs" style="left:430px;top:196px;width:214px;height:180px;background:radial-gradient(ellipse at 50% 55%, #fbfaf4 0%, #e6e2d6 55%, rgba(230,226,214,0) 80%);"></div>
  </section>

  <section class="label label--meat">
    <div class="flames" role="img" aria-label="Red, orange and yellow fire flames rising across the label"></div>
    <div class="cut-line"></div>
    <p class="brand">Brisk Meadow Harvest<sup>TM</sup></p>
    <span class="kicker" style="left:130px;top:94px;">NATURAL</span>
    <span class="flavor" style="left:40px;top:124px;font-size:100px;">Meat&amp;Poultry</span>
    <span class="kicker" style="left:284px;top:246px;">SEASONING</span>
    <div class="badge" style="top:204px;">
      <svg viewBox="0 0 128 128"><polygon points="64,2 76,34 108,16 96,50 126,64 96,78 108,112 76,94 64,126 52,94 20,112 32,78 2,64 32,50 20,16 52,34" fill="var(--burst-yellow)" stroke="var(--burst-edge)" stroke-width="2"/></svg>
      <p class="badge-text">HEALTHY &amp;<br>ALL NATURAL</p>
    </div>
    <div class="food-photo" role="img" aria-label="Photo of raw steak, ribs, chicken and sausage with herbs" style="left:330px;top:276px;width:300px;height:106px;background:radial-gradient(ellipse at 50% 55%, #c8202e 0%, #a31826 50%, rgba(163,24,38,0) 80%);"></div>
  </section>

  <section class="label label--chili">
    <div class="flames" role="img" aria-label="Red, orange and yellow fire flames rising across the label"></div>
    <div class="cut-line"></div>
    <p class="brand">Brisk Meadow Harvest<sup>TM</sup></p>
    <span class="kicker" style="left:196px;top:94px;">NATURAL</span>
    <span class="flavor" style="left:262px;top:118px;font-size:110px;">Chili</span>
    <span class="kicker" style="left:340px;top:224px;">SEASONING</span>
    <div class="badge" style="top:208px;">
      <svg viewBox="0 0 128 128"><polygon points="64,2 76,34 108,16 96,50 126,64 96,78 108,112 76,94 64,126 52,94 20,112 32,78 2,64 32,50 20,16 52,34" fill="var(--burst-yellow)" stroke="var(--burst-edge)" stroke-width="2"/></svg>
      <p class="badge-text">HEALTHY &amp;<br>ALL NATURAL</p>
    </div>
    <div class="food-photo" role="img" aria-label="Photo of red hot chili peppers, whole and sliced" style="left:300px;top:264px;width:320px;height:116px;background:radial-gradient(ellipse at 50% 50%, #e2141c 0%, #b30f16 50%, rgba(179,15,22,0) 80%);"></div>
  </section>

</main>
</body>
</html>
```